QR TILL WORKS , CREDIT CARD PROCESSING EQUIPMENT

qrtillworks is a sub division of Tallow a credit car processing co.
dennis arlow
14 cedar hollow ln
brookvale ny 07312
suite 412

qrtillworks.example
cell 555-214-7730
office 555-861-2093
we sell pos systems to merchant who want to accept credit cards at there retail location.
black card would be nice buit open to different ideas

Target Market(s)

retail merchants

Industry/Entity Type

credit card processing

Contact Information for Business Card

card should include web site phone address

Colors

Designer to choose colors to be used in the design.

Requirements
Should not have
• red

```html
<!DOCTYPE html>
<html lang="en">
<head>
<meta charset="utf-8">
<title>QR Till Works – Business Card</title>
<link href="https://fonts.googleapis.com/css2?family=Lato:wght@400;700&family=Oswald:wght@500&display=swap" rel="stylesheet">
<style>
  :root {
    --backdrop: #6e6e6e;
    --card: #111111;
    --gold: #ddb20a;
    --white: #f2f2f2;
    --silver: #c9c9c9;
  }
  html, body {
    margin: 0;
    width: 1200px;
    height: 1200px;
    overflow: hidden;
    background: var(--backdrop);
  }
  .card {
    position: absolute;
    left: 262px;
    width: 686px;
    height: 392px;
    background: var(--card);
  }
  .card--front { top: 165px; }
  .card--back { top: 653px; }

  .brand {
    position: absolute;
    display: flex;
    align-items: center;
    font-family: "Lato", sans-serif;
    font-weight: 700;
    color: var(--white);
    line-height: 1;
    white-space: nowrap;
  }
  .brand__dot {
    border-radius: 50%;
    background: var(--gold);
    flex: none;
  }
  .card--front .brand {
    left: 100px;
    top: 176px;
    font-size: 27px;
    gap: 10px;
  }
  .card--front .brand__dot { width: 15px; height: 15px; }
  .card--back .brand {
    left: 0;
    right: 0;
    top: 170px;
    justify-content: center;
    font-size: 52px;
    gap: 16px;
    color: var(--silver);
  }
  .card--back .brand__dot { width: 26px; height: 26px; }

  .divider {
    position: absolute;
    left: 377px;
    width: 2px;
  }
  .divider--gold { top: 106px; height: 36px; background: var(--gold); }
  .divider--white { top: 147px; height: 138px; background: var(--white); }

  .contact {
    position: absolute;
    left: 404px;
    top: 102px;
    font-family: "Lato", sans-serif;
    color: var(--white);
  }
  .contact__name {
    margin: 0 0 6px;
    font-family: "Oswald", sans-serif;
    font-weight: 500;
    font-size: 27px;
    letter-spacing: 0.5px;
    color: var(--gold);
    text-transform: uppercase;
    line-height: 1.2;
  }
  .contact__address {
    margin: 0 0 10px;
    font-style: normal;
    font-size: 17px;
    line-height: 21.5px;
  }
  .contact__list {
    list-style: none;
    margin: 0;
    padding: 0;
    font-size: 17px;
    line-height: 21.5px;
  }
  .contact__list li {
    display: flex;
    align-items: center;
    gap: 9px;
  }
  .contact__icon {
    width: 15px;
    height: 15px;
    flex: none;
    fill: var(--gold);
  }

  .accent-bar {
    position: absolute;
    bottom: 0;
    height: 12px;
  }
  .accent-bar--gold { left: 0; width: 352px; background: var(--gold); }
  .accent-bar--white { left: 355px; right: 0; background: #e8e8e8; }
</style>
</head>
<body>

<section class="card card--front">
  <div class="brand">
    <span class="brand__dot"></span>
    <span class="brand__name">QR TILL WORKS</span>
  </div>

  <span class="divider divider--gold"></span>
  <span class="divider divider--white"></span>

  <div class="contact">
    <h1 class="contact__name">Dennis Arlow</h1>
    <address class="contact__address">
      14 cedar hollow ln<br>
      brookvale ny 07312<br>
      suite 412
    </address>
    <ul class="contact__list">
      <li>
        <svg class="contact__icon" viewBox="0 0 16 16" aria-hidden="true">
          <path d="M3.6 1.2l2.3 2.9-1.4 1.6c.9 2 2.4 3.6 4.4 4.6l1.6-1.4 2.9 2.3-1.3 2.4C7.4 13.5 2.3 8.4 1.2 3z"/>
        </svg>
        <span>555-861-2093</span>
      </li>
      <li>
        <svg class="contact__icon" viewBox="0 0 16 16" aria-hidden="true">
          <path d="M4 0h8a1 1 0 0 1 1 1v14a1 1 0 0 1-1 1H4a1 1 0 0 1-1-1V1a1 1 0 0 1 1-1zm1 2v10h6V2zm3 11a1 1 0 1 0 0 2 1 1 0 0 0 0-2z"/>
        </svg>
        <span>555-214-7730</span>
      </li>
      <li>
        <svg class="contact__icon" viewBox="0 0 16 16" aria-hidden="true">
          <circle cx="8" cy="8" r="7"/>
          <path d="M5 4c2 0 2 2 3 3s-1 2-2 2-1 2 0 3M10 4c0 1 1 2 2 2" stroke="#111" stroke-width="1.3" fill="none"/>
        </svg>
        <span>qrtillworks.example</span>
      </li>
    </ul>
  </div>
</section>

<section class="card card--back">
  <div class="brand">
    <span class="brand__dot"></span>
    <span class="brand__name">QR TILL WORKS</span>
  </div>
  <span class="accent-bar accent-bar--gold"></span>
  <span class="accent-bar accent-bar--white"></span>
</section>

</body>
</html>
```